Amber Ladle Wishes Website Design; Cupcake Business with a unique and bespoke design element

We need a website design for a new bespoke and unique business making gourmet cupcakes - but MOST IMPORTANTLY we design and handmake cupcake wrappers and toppers specifically for each client's event. We are based in Sydney, Australia. The final resulting website should be elegant yet whimsical reflecting the notion of dreams and very elegant events eg weddings and very special parties.

We want to eventually have about 5 pages, HOWEVER, this project is specifically for the first page (ie Home page) and one other only. The final required pages are: a HOME page; ABOUT US page; PHOTO GALLERY page; FLAVOUR MENU & OTHER PRODUCTS page; CONTACT & INTERNET ENQUIRY page.

We expect the HOME page to be quite elaborate, perhaps including some animation. We will be providing the text content for all the other pages, and basically they will have the same background as the home page. We are looking for a clean design that runs across each page thus giving the website a continuity that pulls it all together. We would like our logo to be included on each page.

PLEASE NOTE: We will want multiple pages worked on in the handover phase but initially we want a very concise, consistent template to limit the amount of work to prospective designers.

While we are primarily looking for the design phase to be covered by this project, we would certainly appreciate coding to be included and will take that into consideration when choosing a winner.

Hi Designers

We have added some more information to our brief - please review it.

Thanks and happy designing

Hi Designers

Please note that we have increased our Prize money to $750.00.  We hope this encourages you to participate.

Thanks and regards
Amber Ladle Wishes

Hi Designers

We've just posted some photos to help give you an idea of what we do.  Please note our attention to detail and precision in our work.

Thanks
Amber Ladle Wishes

Hi Designers

Please Note:  What makes us different  to any other cupcake business is that we design cupcake wrappers and toppers, unique to our client's event whether it be a wedding, a birthday party or product launch.  We consult with our client to understand themes, colours, styles etc.  We then have our designs printed, next they are cut by a specialised computerised cutting machine,  We assemble everything by hand, and usually embellish the wrapper and topper with pearls, crystals, feathers, lace, ribbons or whatever else is appropriate for the event.  All work is totally bespoke, unique and individual.  No other cupcake supplier that we know of goes to these lengths to satisfy their client's dreams.

THE WRAPPER AND TOPPER IS OUR PRIMARY SELLING POINT. 

PLEASE NOTE:- We have uploaded a new photograph which we want to be used as the main photograph on the landing page.

We have removed all previous photographs of cupcakes (except for one that we can't get rid of).

We don't want a picture of a cupcake on the landing page we want the image _D7C3239.jpg to be used for that purpose.

We have also uploaded our logo in a number of file formats as we have had requests from you for these.

Hi designers

we have a crazy busy weekend on and won't be able to make any decisions re our competition until Monday  -  sorry to keep you in suspense, just a couple more days please!

regards
Meg

Target Market(s)

Primarily women - brides, new mothers (Christenings), Event Planners, who place an emphasis on the beauty of a product rather than the cost

Industry/Entity Type

Events

Requirements
Must have
• It must have our Logo (see attached upload) on each page (our logo is a butterfly atop a cupcake resting on a spoon and our motto is "Creating Delicious Works of Art". The colours used are pale pink, blue and chocolate brown and we'd expect these colours to be repeated in the final website.
The website must have a photo gallery which we can access and add to/change as our business grows.
We need a contact page which has an "internet enquiry form".
There should be a "Menu" page describing our cupcake flavours.
The Home page must have a party/event feel to it - definitely making an enquirer want to enter further into the site.
Nice to have
• Our logo is attached below in the "uploads". One idea that we have had is to use the butterfly in the logo but start it as a caterpillar crawling on the screen; as it spins it's cocoon the words "Sweet Dreams Little Caterpillar" would appear on screen; this would incorporate the "Dreams" in our Business Name; then our logo butterfly would hatch. This encapsulates the idea of taking something plain (caterpillar/cupcake) and creating something beautiful (butterfly/OUR cupcake).
However, we are open to other design ideas.
The colours we would like to have are pale pink, blue and chocolate brown in the design.

Some websites we really admire are: www.dorawillow.com www.thimblereedtart.com.au and www.greetingsvera.com.au
These websites have a lightness and sense of fantasy to them. They do not convey a corporate image at all, rather they make you want to be at the party.
Should not have
• No "Corporate" style.

Most Important: We already have a website which we are not happy with - that is why we are going through this exercise to replace it. That means we DO NOT want anything along the lines of our current website. We are expecting some fresh ideas for our prize money.

```html
<!DOCTYPE html>
<html lang="en">
<head>
<meta charset="utf-8">
<title>Amber Ladle Wishes</title>
<link rel="stylesheet" href="https://fonts.googleapis.com/css2?family=Noto+Sans:wght@400;700&display=swap">
<style>
  :root {
    --header-top: #fde3e7;
    --header-bottom: #fbd3da;
    --page-pink: #fbdde2;
    --logo-panel: #fde9ed;
    --button-face: #fbe0e5;
    --button-edge: #fff3f5;
    --button-text: #3e4b5b;
    --title-blue: #1b7bc9;
    --body-text: #1c1c1c;
    --cocoa: #5e3a2c;
    --rose: #e8578a;
    --footer-pink: #f9abb6;
    --pager-face: #fdf0f2;
  }
  * { box-sizing: border-box; margin: 0; padding: 0; }
  html, body { width: 1200px; height: 1043px; overflow: hidden; }
  body {
    position: relative;
    background: var(--page-pink);
    font-family: "Noto Sans", Verdana, sans-serif;
    color: var(--body-text);
  }
  .site-header {
    position: absolute; left: 0; top: 0; width: 1200px; height: 252px;
    background: linear-gradient(180deg, var(--header-top), var(--header-bottom));
  }
  .brand {
    position: absolute; left: 70px; top: 45px; width: 321px; height: 172px;
    background: var(--logo-panel);
    display: flex; align-items: center; justify-content: center; gap: 12px;
  }
  .brand-dot { width: 18px; height: 18px; border-radius: 50%; background: var(--rose); }
  .brand-name { font-size: 25px; font-weight: 700; color: var(--cocoa); }
  .main-nav a {
    position: absolute; top: 182px; width: 219px; height: 37px;
    display: flex; align-items: center; justify-content: center;
    background: var(--button-face);
    border: 2px solid var(--button-edge);
    border-radius: 4px;
    box-shadow: 0 1px 3px rgba(200,120,135,.35);
    color: var(--button-text); font-size: 14px; font-weight: 700;
    letter-spacing: 1.2px; text-decoration: none;
  }
  .nav-menu { left: 408px; }
  .nav-gallery { left: 639px; }
  .nav-enquiry { left: 872px; }
  .hero-photo {
    position: absolute; left: 70px; top: 252px; width: 500px; height: 707px;
    background: linear-gradient(180deg, #f4e8ea 0%, #f1c9d1 45%, #ea9fb3 80%, #e2809d 100%);
  }
  .pager {
    position: absolute; left: 404px; top: 961px; display: flex; gap: 3px;
  }
  .pager span {
    width: 31px; height: 21px; background: var(--pager-face);
    display: flex; align-items: center; justify-content: center;
    font-size: 15px; font-weight: 700; color: #222;
  }
  .intro { position: absolute; left: 600px; top: 280px; width: 494px; }
  .intro h1 {
    margin-left: 66px; font-size: 29px; font-weight: 700; letter-spacing: 1px;
    color: var(--title-blue); line-height: 34px;
  }
  .intro .tagline {
    margin-left: 68px; font-size: 13px; font-weight: 700; letter-spacing: .6px;
    line-height: 16px;
  }
  .intro p { font-size: 14px; line-height: 17px; margin-top: 17px; }
  .intro .tagline + p { margin-top: 23px; }
  .site-footer {
    position: absolute; left: 0; top: 982px; width: 1200px; height: 61px;
    background: var(--footer-pink); font-size: 14.5px; color: #2a2a2a;
  }
  .footer-links { position: absolute; left: 105px; top: 19px; }
  .copyright { position: absolute; right: 69px; top: 17px; }
</style>
</head>
<body>
  <header class="site-header">
    <div class="brand"><span class="brand-dot"></span><span class="brand-name">Amber Ladle Wishes</span></div>
    <nav class="main-nav">
      <a class="nav-menu" href="#">FLAVOUR MENU</a>
      <a class="nav-gallery" href="#">PHOTO GALLERY</a>
      <a class="nav-enquiry" href="#">INTERNET ENQUIRY</a>
    </nav>
  </header>

  <div class="hero-photo" role="img" aria-label="Photo of a tiered stand of cupcakes with pink tutu dress toppers and a birthday number candle"></div>
  <div class="pager"><span>1</span><span>2</span><span>3</span><span>4</span><span>5</span></div>

  <main class="intro">
    <h1>AMBER LADLE WISHES</h1>
    <p class="tagline">CREATING DELICIOUS WORKS OF ART</p>
    <p>Amber Ladle Wishes is a gourmet cupcake service based in Wrenfield, Sydney, specialising in artistic creations focusing heavily on design, colour, theme and most importantly taste!</p>
    <p>We handcraft the best cupcakes that you have ever tasted and they're beautiful too. Our cupcake toppers and wrappers are designed personally for your event making them a unique work of art that have the WOW factor. It's not just a cupcake - Amber Ladle Wishes are indulgent, luxurious, chic and delicious.</p>
    <p>We are experts in selecting just the right colours and accents to match your colour palette, theme, or company logo. Everything we do is completely bespoke and we use colour/fabric swatches, floral arrangements, invitations or even just an idea to create a display at your event which will have your guests talking for weeks! We work with you every step of the way to make sure that your cupcakes will not only meet your requirements but exceed your expectations too.</p>
  </main>

  <footer class="site-footer">
    <div class="footer-links">Products &nbsp;/ Menu Gallery &nbsp;/ &nbsp;FAQ &amp; Testimonails Contact</div>
    <div class="copyright">© Copyright Amber Ladle Wishes 2011</div>
  </footer>
</body>
</html>
```